Los Angeles based Demolition, Grading, and Structural concrete Contractor in need of a Sale brochure

We are a Los Angeles-based demolition, grading, and structural concrete contractor looking for a professionally designed sales brochure that represents our company and services. The brochure should be visually appealing, easy to read, and include the following:

-Company Logo: Prominently displayed to enhance brand identity.

-Services We Offer: A clear breakdown of our key services, including demolition, grading, and structural concrete work.

-Project Scope & Capabilities: A brief explanation of the type of projects we handle (residential, commercial, industrial).

-Pricing Information: Mention that demolition services start at $20,000. This price includes complete demolition of structure, safe debris removal and hauling, site preparation for new construction.

-Contact Information: Our phone number(555.206.1187), email(contact@bravoridgebuilders.example) , and website for potential clients to reach out.

The design should reflect the professionalism and strength of our industry, using a modern, clean layout with bold colors that align with construction and demolition themes. Images of past work or stock photos representing our services are encouraged.

Final deliverables should be print-ready (PDF) and digital-friendly formats. Looking forward to creative and impactful designs!

```html
<!DOCTYPE html>
<html lang="en">
<head>
<meta charset="utf-8">
<title>Bravo Ridge Builders – Sales Brochure</title>
<link href="https://fonts.googleapis.com/css2?family=Barlow:wght@400;500;600;800&family=Barlow+Condensed:wght@500;600;700&display=swap" rel="stylesheet">
<style>
:root{
  --page:#efefef;
  --blue:#1272bb;
  --navy:#0e1a33;
  --white:#ffffff;
  --ink:#111111;
  --grey:#7a7f86;
}
*{margin:0;padding:0;box-sizing:border-box}
html,body{width:721px;height:1200px;overflow:hidden;background:var(--page)}
.canvas{position:relative;width:721px;height:1200px;background:var(--page)}
.brochure{
  position:absolute;left:87px;top:107px;width:1124px;height:794px;
  transform:scale(0.486);transform-origin:0 0;
  background:var(--white);overflow:hidden;
  box-shadow:30px 40px 40px rgba(0,0,0,.35);
  font-family:"Barlow",sans-serif;color:var(--ink);
}
.shapes{position:absolute;inset:0}
.abs{position:absolute}
.who-title{left:578px;top:14px;font-weight:800;font-size:66px;line-height:62px;letter-spacing:1px}
.who-title .who{color:var(--blue)}
.who-title .we{color:var(--navy)}
.divider{left:852px;top:20px;width:2px;height:125px;background:var(--navy)}
.brand{left:876px;top:44px;font-weight:800;font-size:31px;line-height:36px;color:var(--blue);letter-spacing:1px;white-space:nowrap}
.who-text{left:584px;top:156px;font-size:11.5px;font-weight:500;line-height:18.8px;white-space:nowrap}
.services-title{left:35px;top:336px;color:var(--navy);font-weight:600;font-size:46px;line-height:44px}
.services-title span{display:block;color:var(--white);font-weight:500;font-size:30px;line-height:30px}
.services-title span::after{content:"";display:inline-block;width:32px;height:2px;background:var(--white);vertical-align:middle;margin-left:4px}
.service h3{font-family:"Barlow Condensed",sans-serif;font-weight:700;font-size:21px;color:var(--navy);line-height:22px;margin-bottom:4px;white-space:nowrap}
.service h3::before{content:"";display:inline-block;width:16px;height:16px;background:var(--navy);margin-right:3px;vertical-align:-1px}
.service p{font-size:10.6px;font-weight:500;line-height:15.6px;color:var(--white);white-space:nowrap}
.demolition{left:115px;top:420px}
.concrete{left:302px;top:547px}
.grading{left:592px;top:547px}
.contact-tag{left:36px;top:632px;width:143px;height:38px;background:var(--navy);color:var(--white);font-size:24px;font-weight:500;padding:5px 7px;line-height:28px}
.phone{left:35px;top:676px;font-size:33px;font-weight:500;color:var(--navy);line-height:34px;white-space:nowrap}
.phone svg{vertical-align:middle;margin-left:4px}
.handle{left:35px;top:709px;font-size:29px;font-weight:500;color:var(--navy);line-height:32px;white-space:nowrap}
.handle i{display:inline-block;width:18px;height:18px;background:var(--navy);border-radius:4px;vertical-align:middle;margin-left:6px}
.web-bar{left:36px;top:746px;width:430px;height:32px;background:linear-gradient(90deg,var(--blue),#6fb0e0 75%,rgba(255,255,255,0));color:var(--navy);font-size:11px;font-weight:500;line-height:32px;padding-left:6px;white-space:nowrap}
.web-bar b{display:inline-block;width:7px;height:7px;border-radius:50%;background:var(--navy);margin-right:3px}
.web-bar s{display:inline-block;width:7px;height:5px;background:var(--navy);margin:0 3px 0 6px;text-decoration:none}
.pricing{right:46px;top:634px;text-align:right;font-weight:800;font-size:30px;line-height:30px;color:var(--navy)}
.pricing .lead{color:var(--blue)}
.pricing-text{right:46px;top:703px;text-align:right;font-family:"Barlow Condensed",sans-serif;font-weight:500;font-size:15px;line-height:20px;color:var(--blue);white-space:nowrap}
.pricing-text strong{color:var(--navy);font-size:18px;font-weight:700}
</style>
</head>
<body>
<div class="canvas">
  <article class="brochure">
    <svg class="shapes" width="1124" height="794" viewBox="0 0 1124 794">
      <defs>
        <linearGradient id="siteGrad" x1="0" y1="0" x2="1" y2="1">
          <stop offset="0" stop-color="#c9b79a"/><stop offset="1" stop-color="#a8967a"/>
        </linearGradient>
        <linearGradient id="digGrad" x1="0" y1="0" x2="0" y2="1">
          <stop offset="0" stop-color="#6fa8dc"/><stop offset=".55" stop-color="#b9cfe0"/><stop offset=".75" stop-color="#d68a2c"/><stop offset="1" stop-color="#6b5a48"/>
        </linearGradient>
      </defs>
      <polygon points="0,255 150,322 562,550 1124,240 1124,520 910,642 482,794 0,520" fill="var(--blue)"/>
      <polygon points="240,278 562,430 730,345 730,250 562,350 260,275" fill="var(--white)"/>
      <polygon points="240,278 262,276 562,445 730,352 730,372 562,465" fill="var(--grey)"/>
      <polygon points="165,300 240,280 562,480 730,385 730,445 562,550" fill="var(--navy)"/>
      <polygon points="400,345 470,345 562,400 562,430" fill="var(--blue)"/>
      <polygon points="0,0 438,0 438,145 140,320 0,245" fill="url(#siteGrad)" role="img" aria-label="Aerial photo of a foundation site with rebar footings and machinery"/>
      <g transform="translate(450,266)">
        <polygon points="0,-88 76,-44 76,44 0,88 -76,44 -76,-44" fill="var(--blue)"/>
        <polygon points="0,-76 66,-38 66,38 0,76 -66,38 -66,-38" fill="var(--navy)"/>
        <g fill="none" stroke="var(--white)" stroke-width="3">
          <rect x="-44" y="-10" width="88" height="38" rx="3"/>
          <line x1="-10" y1="-40" x2="-10" y2="28"/><line x1="10" y1="-40" x2="10" y2="28"/><line x1="30" y1="-40" x2="30" y2="28"/>
          <line x1="-24" y1="-24" x2="40" y2="-24"/><line x1="-24" y1="0" x2="40" y2="0"/>
        </g>
      </g>
      <g transform="translate(1008,218)">
        <polygon points="0,-78 68,-39 68,39 0,78 -68,39 -68,-39" fill="var(--blue)"/>
        <polygon points="0,-67 58,-33 58,33 0,67 -58,33 -58,-33" fill="var(--navy)" role="img" aria-label="Excavator line icon"/>
      </g>
      <polygon points="906,250 1078,345 1078,522 908,642 735,525 735,340" fill="var(--white)"/>
      <polygon points="906,256 1073,348 1073,519 908,636 740,522 740,343" fill="url(#digGrad)" role="img" aria-label="Photo of an orange excavator on a site at sunset with city skyline"/>
    </svg>

    <h1 class="abs who-title"><span class="who">WHO</span><br><span class="we">WE ARE</span></h1>
    <div class="abs divider"></div>
    <div class="abs brand">BRAVO RIDGE<br>BUILDERS</div>
    <p class="abs who-text">Bravo Ridge Builders, established in 2019, is a leading construction<br>firm committed to excellence and innovation. We specialize in<br>high-quality residential and commercial projects, prioritizing<br>safety, sustainability, and efficiency. Our mission is to build<br>lasting client relationships through open communication and<br>collaboration. With a skilled team and cutting-edge<br>practices, we transform visions into enduring<br>spaces, ensuring quality and trust in<br>every project.</p>

    <h2 class="abs services-title">OUR<span>SERVICES</span></h2>
    <section class="abs service demolition">
      <h3>DEMOLITION</h3>
      <p>Bravo Ridge provides safe and efficient<br>demolition services for projects of all sizes. Using<br>advanced equipment and skilled professionals, we<br>ensure regulatory compliance and minimal environ-<br>mental impact. Committed to responsible waste<br>management, we pave the way for future develop-<br>ments with precision and care.</p>
    </section>
    <section class="abs service concrete">
      <h3>STRUCTURAL CONCRETE</h3>
      <p>Bravo Ridge specializes in structural concrete<br>and foundations, including slab-on-grade,<br>shoring, retaining walls, and hillside<br>basements. Using advanced techniques and<br>quality materials, we ensure stability, durabili-<br>ty, and safety, providing strong foundations for<br>all construction projects.</p>
    </section>
    <section class="abs service grading">
      <h3>GRADING</h3>
      <p>Bravo Ridge offers expert site grading,<br>excavation, and hauling services, ensuring a<br>strong foundation for any project. Using<br>advanced equipment, we optimize soil<br>removal, leveling, and site preparation with<br>precision and safety. Our commitment to<br>quality and efficiency makes us a trusted<br>partner for residential, commercial, and<br>industrial developments.</p>
    </section>

    <div class="abs contact-tag">CONTACT</div>
    <div class="abs phone">555.206.1187<svg width="22" height="22" viewBox="0 0 24 24"><path d="M6 3l4 4-2 3c1 2 3 4 5 5l3-2 4 4-3 3C10 20 4 14 3 6z" fill="var(--navy)"/></svg></div>
    <div class="abs handle">bravoridge_builders<i></i></div>
    <div class="abs web-bar"><b></b>www.bravoridgebuilders.example<s></s>contact@bravoridgebuilders.example</div>

    <h2 class="abs pricing"><span class="lead">PRICING</span><br>INFORMATION</h2>
    <p class="abs pricing-text">demolition services start at <strong>$20,000.</strong> This price<br>includes complete demolition of structure, safe<br>debris removal and hauling, site preparation for<br>new construction</p>
  </article>
</div>
</body>
</html>
```